PDN Letterhead

We need a letterhead design that will be able to be used on all marketing products (letterhead, mail chimp, envelops, business cards, etc.) We are a law firm specializing primarily in transportation law but offer a wide range of services to our clients. We would like the design to be modern, simple, and professional. Our colors are black and gold, however, we've incorporated dark gray and white on other marketing products such as our website.

```html
<!DOCTYPE html>
<html lang="en">
<head>
<meta charset="utf-8">
<title>PDN Law Group Letterhead</title>
<link href="https://fonts.googleapis.com/css2?family=Cinzel:wght@400&family=Open+Sans:wght@400&display=swap" rel="stylesheet">
<style>
  :root {
    --backdrop: #c4c6c9;
    --paper: #ffffff;
    --ink: #111111;
    --gold: #b39a72;
    --text-gray: #4a4a4a;
    --corner-sand: #f2eee8;
    --corner-gray: #d9d9d9;
  }
  html, body {
    margin: 0;
    width: 1058px;
    height: 1200px;
    overflow: hidden;
    background: var(--backdrop);
  }
  .letterhead {
    position: absolute;
    left: 70px;
    top: 10px;
    width: 918px;
    height: 1180px;
    background: var(--paper);
    overflow: hidden;
  }
  .brand {
    position: absolute;
    left: 33px;
    top: 46px;
    width: 168px;
    text-align: center;
    font-family: "Cinzel", serif;
    font-weight: 400;
    color: var(--ink);
  }
  .brand-square {
    display: block;
    width: 34px;
    height: 34px;
    margin: 0 auto 16px;
    background: var(--gold);
  }
  .brand-name {
    display: block;
    font-size: 46px;
    line-height: 1;
    letter-spacing: 2px;
  }
  .brand-sub {
    display: block;
    margin-top: 10px;
    font-size: 19px;
    line-height: 1;
    letter-spacing: 4px;
    color: var(--gold);
  }
  .contact {
    position: absolute;
    left: 708px;
    top: 28px;
    font-family: "Open Sans", sans-serif;
    font-style: normal;
    color: var(--text-gray);
  }
  .contact-firm {
    margin: 0 0 3px;
    font-size: 16px;
    font-weight: 400;
    color: var(--gold);
  }
  .contact-address {
    margin: 0 0 5px;
    font-size: 11.5px;
    line-height: 15px;
  }
  .contact-list {
    list-style: none;
    margin: 0;
    padding: 0;
    font-size: 11.5px;
  }
  .contact-list li {
    display: flex;
    align-items: center;
    height: 17.5px;
  }
  .contact-list svg {
    width: 11px;
    height: 11px;
    margin-right: 9px;
    flex: none;
  }
  .corner {
    position: absolute;
    bottom: 0;
    width: 200px;
    height: 200px;
  }
  .corner-left {
    left: 0;
    background: radial-gradient(circle at 0% 100%, var(--corner-sand) 0%, rgba(242,238,232,0.6) 45%, rgba(255,255,255,0) 72%);
  }
  .corner-right {
    right: 0;
    background: radial-gradient(circle at 100% 100%, var(--corner-gray) 0%, rgba(217,217,217,0.6) 45%, rgba(255,255,255,0) 72%);
  }
</style>
</head>
<body>
<main class="letterhead">
  <div class="brand">
    <span class="brand-square"></span>
    <span class="brand-name">PDN</span>
    <span class="brand-sub">LAW GROUP</span>
  </div>

  <address class="contact">
    <p class="contact-firm">PDN Law Group</p>
    <p class="contact-address">240 Harbor Crest Avenue, Suite<br>310 Riverton, FL 33990</p>
    <ul class="contact-list">
      <li>
        <svg viewBox="0 0 12 12" aria-hidden="true"><path d="M1 4 Q6 0 11 4 L9.5 5.5 L8 4.5 L4 4.5 L2.5 5.5 Z M3 6 H9 L10 11 H2 Z" fill="#b39a72"/></svg>
        555.014.2290
      </li>
      <li>
        <svg viewBox="0 0 12 12" aria-hidden="true"><rect x="0.5" y="2.5" width="11" height="7" fill="none" stroke="#b39a72"/><path d="M0.5 2.5 L6 7 L11.5 2.5" fill="none" stroke="#b39a72"/></svg>
        admin@pdnlawgroup.com
      </li>
      <li>
        <svg viewBox="0 0 12 12" aria-hidden="true"><circle cx="6" cy="6" r="5" fill="none" stroke="#b39a72"/><ellipse cx="6" cy="6" rx="2.2" ry="5" fill="none" stroke="#b39a72"/><path d="M1 6 H11" stroke="#b39a72"/></svg>
        www.pdnlawgroup.com
      </li>
    </ul>
  </address>

  <div class="corner corner-left" role="img" aria-label="Soft sand-toned corner accent"></div>
  <div class="corner corner-right" role="img" aria-label="Soft gray corner accent"></div>
</main>
</body>
</html>
```